Ember Ridge Grilling Society

The current website is ergsgrill.com. We want to change the color scheme to the gold/white and black in the logo. Front page elements include everything we have except the social media links at the top can go to the bottom. We need to add fliers like http://ergsgrill.com/content/fliers/2022/SmartSelect_20211215-123241_Slides.jpg to the front page. There are more available on the events page. Also a place for a main news story on the front page. All the sponsor logos need to be present on every page. I have added a couple of more sponsor logos. On the about us page we will want to add a contact list and email form. We will take care of all functionality. You provide only design.
One site we like is tpfl.us for it is easy to navigate.
Target Market(s)
People interested in competition BBQ
Coding
Coded - Design and coding required
Number of Pages Required
5+ page
Look and feel
Each slider illustrates characteristics of the customer's brand and the style your logo design should communicate.

```html
<!DOCTYPE html>
<html lang="en">
<head>
<meta charset="utf-8">
<title>Ember Ridge Grilling Society</title>
<link href="https://fonts.googleapis.com/css2?family=Montserrat:wght@400;500;600;700&family=Questrial&display=swap" rel="stylesheet">
<style>
:root{
  --gold:#efd272;
  --gold-deep:#d9b648;
  --page:#f3f3f3;
  --band:#e6e6e6;
  --white:#ffffff;
  --ink:#2b2b2b;
  --dark:#222222;
  --dark-2:#333333;
  --muted:#555555;
}
*{margin:0;padding:0;box-sizing:border-box}
html,body{width:1200px;height:3601px;overflow:hidden}
body{position:relative;background:var(--page);font-family:'Questrial',sans-serif;color:var(--ink)}
.abs{position:absolute}
.brand{left:0;width:1200px;top:44px;text-align:center}
.brand-name{font-family:'Montserrat',sans-serif;font-weight:500;font-size:30px;letter-spacing:2px;color:var(--gold-deep)}
.brand-sub{font-family:'Montserrat',sans-serif;font-weight:700;font-size:10px;letter-spacing:4px;color:var(--ink);margin-top:2px}
.nav{left:70px;width:1062px;top:143px;display:flex;justify-content:space-between;font-family:'Montserrat',sans-serif;font-size:12px;letter-spacing:3px;color:var(--ink)}
.hero{left:0;top:196px}
.hero-title{left:66px;top:370px;font-family:'Montserrat',sans-serif;font-weight:500;font-size:35px;line-height:50px;letter-spacing:4px;color:var(--ink)}
.hero-text{left:66px;top:488px;width:360px;font-family:'Montserrat',sans-serif;font-size:14px;line-height:25.5px;letter-spacing:1.5px;color:var(--ink)}
.section-title{left:0;width:1200px;text-align:center;font-family:'Montserrat',sans-serif;font-weight:600;font-size:22px;letter-spacing:4px;color:var(--ink)}
.standings{font-size:23px;letter-spacing:3px;color:var(--ink)}
.standings .c{position:absolute;white-space:nowrap}
.tab{top:1322px;width:210px;height:66px;background:var(--gold);display:flex;align-items:center;justify-content:center;font-family:'Montserrat',sans-serif;font-size:15px;letter-spacing:2px;color:var(--ink)}
.white-band{left:0;width:1200px;background:var(--white)}
.sponsor{width:200px;height:160px;display:flex;align-items:center;justify-content:center;font-family:'Montserrat',sans-serif;font-weight:600;font-size:21px;line-height:28px;text-align:center;color:var(--ink);letter-spacing:1px}
.event-box{left:67px;top:1833px;width:560px;height:476px;background:var(--gold);text-align:center}
.event-box p{margin-top:173px;font-size:25px;line-height:27px;letter-spacing:3px;color:var(--ink)}
.enroll{display:inline-block;margin-top:32px;width:211px;height:66px;line-height:66px;background:var(--dark-2);color:var(--white);font-family:'Montserrat',sans-serif;font-size:15px;letter-spacing:2px}
.story{left:650px;width:483px;height:226px;background:linear-gradient(135deg,#4a4a4a,#6c6a66 45%,#3d3d3d)}
.story span{position:absolute;left:117px;top:100px;font-size:20px;line-height:26px;letter-spacing:3px;color:var(--gold)}
.see-more{left:0;width:1200px;top:2336px;text-align:center;font-family:'Montserrat',sans-serif;font-size:13px;letter-spacing:2px;text-decoration:underline;color:var(--ink)}
.compete{left:0;top:2378px;width:1200px;height:401px;background:var(--band);text-align:center}
.compete h2{margin-top:102px;font-family:'Montserrat',sans-serif;font-weight:600;font-size:26px;letter-spacing:5px}
.compete p{margin-top:22px;font-size:17px;line-height:23px;letter-spacing:2.5px;color:var(--muted)}
.compete a{display:inline-block;margin-top:30px;width:232px;height:66px;line-height:66px;background:var(--gold);font-family:'Montserrat',sans-serif;font-size:14px;letter-spacing:2px;color:var(--ink);text-decoration:none}
.foot-left{left:0;top:3203px;width:613px;height:398px;background:var(--dark)}
.foot-right{left:613px;top:3203px;width:587px;height:398px;background:var(--dark-2)}
.about{left:67px;top:3272px;width:520px;font-family:'Montserrat',sans-serif;font-weight:600;font-size:13.5px;line-height:25.5px;letter-spacing:1px;color:var(--white)}
.rule{left:67px;top:3424px;width:464px;height:1px;background:#cfcfcf}
.social{left:67px;top:3458px;display:flex;gap:18px;align-items:center;font-family:'Montserrat',sans-serif;font-weight:600;font-size:13px;color:var(--white);letter-spacing:1px}
.social i{display:inline-block;width:8px;height:8px;border-radius:50%;background:var(--gold);margin-right:6px;vertical-align:middle}
.contact{left:613px;width:587px;top:3271px;text-align:center;font-family:'Montserrat',sans-serif;font-weight:600;font-size:13.5px;line-height:26px;letter-spacing:1.5px;color:var(--white)}
.contact .gap{height:25px}
.informed{left:734px;top:3452px;font-family:'Montserrat',sans-serif;font-weight:700;font-size:13px;letter-spacing:2px;color:var(--gold)}
.email{left:716px;top:3490px;width:213px;height:44px;border-radius:22px;background:var(--white)}
.email span{position:absolute;left:32px;top:14px;font-size:11px;letter-spacing:2px;color:#aaa}
.email .go{position:absolute;right:0;top:0;width:44px;height:44px;border-radius:50%;background:var(--gold)}
</style>
</head>
<body>

<header>
  <div class="abs brand">
    <div class="brand-name">EMBER RIDGE</div>
    <div class="brand-sub">GRILLING SOCIETY</div>
  </div>
  <nav class="abs nav">
    <span>HOME</span><span>EVENTS</span><span>RESULTS</span><span>TEAM OF THE YEAR</span><span>ABOUT ERGS</span><span>MEMBERS</span><span>SANCTIONING FORM</span>
  </nav>
</header>

<svg class="abs hero" width="1200" height="622" viewBox="0 0 1200 622" role="img" aria-label="Flames rising from meat cooking on a grill">
  <defs>
    <linearGradient id="heroFill" x1="0" y1="0" x2="1" y2="0">
      <stop offset="0" stop-color="#efd272"/>
      <stop offset="0.38" stop-color="#efd272"/>
      <stop offset="0.62" stop-color="#e6bd6a"/>
      <stop offset="0.8" stop-color="#a9a59a"/>
      <stop offset="1" stop-color="#6f8e93"/>
    </linearGradient>
  </defs>
  <polygon points="0,0 455,0 601,35 839,0 1200,0 1200,564 797,564 601,622 406,564 0,564" fill="url(#heroFill)"/>
</svg>
<h1 class="abs hero-title">JOIN THOUSAND<br>OF CHEIF</h1>
<p class="abs hero-text">Lorem ipsum dolor sit amet, consectetur adipiscing elit. Sed vehicula hendrerit commodo. Duis scelerisque, neque vel auctor lobortis, eros arcu malesuada est, a accumsan nibh</p>

<h2 class="abs section-title" style="top:882px">TEAM OF THE YEAR</h2>
<div class="standings">
  <span class="c" style="left:205px;top:964px">Rank</span>
  <span class="c" style="left:423px;top:964px">Team</span>
  <span class="c" style="left:732px;top:964px">Points</span>
  <span class="c" style="left:937px;top:964px">Contest</span>

  <span class="c" style="left:232px;top:1032px">1</span><span class="c" style="left:379px;top:1030px">Hickory Hollow BBQ</span><span class="c" style="left:730px;top:1032px">1491</span><span class="c" style="left:986px;top:1032px">3</span>
  <span class="c" style="left:232px;top:1079px">2</span><span class="c" style="left:379px;top:1079px">Las Brasas</span><span class="c" style="left:730px;top:1079px">1253</span><span class="c" style="left:986px;top:1081px">3</span>
  <span class="c" style="left:232px;top:1126px">3</span><span class="c" style="left:379px;top:1124px">Coal Country Grillers</span><span class="c" style="left:730px;top:1126px">1215</span><span class="c" style="left:986px;top:1130px">3</span>
  <span class="c" style="left:232px;top:1174px">4</span><span class="c" style="left:379px;top:1169px">Aunt Marla's BBQ</span><span class="c" style="left:730px;top:1174px">1075</span><span class="c" style="left:986px;top:1179px">2</span>
  <span class="c" style="left:232px;top:1221px">5</span><span class="c" style="left:379px;top:1219px">Pembrook's BBQ</span><span class="c" style="left:730px;top:1221px">983</span><span class="c" style="left:986px;top:1228px">3</span>
</div>
<div class="abs tab" style="left:71px">Overall</div>
<div class="abs tab" style="left:354px">Brisket</div>
<div class="abs tab" style="left:636px">Ribs</div>
<div class="abs tab" style="left:918px">Chicken</div>

<section class="abs white-band" style="top:1427px;height:951px"></section>
<div class="abs sponsor" style="left:40px;top:1507px">Lantern Creek<br>Spirits</div>
<div class="abs sponsor" style="left:328px;top:1507px">Red Mesa<br>Rubs</div>
<div class="abs sponsor" style="left:619px;top:1507px">Prairie Cut<br>Meats</div>
<div class="abs sponsor" style="left:929px;top:1507px">Smokehouse<br>Sauce Co.</div>

<h2 class="abs section-title" style="top:1748px">NEWS AND EVENTS</h2>
<div class="abs event-box">
  <p>New event start in 2 days<br>Get your teams ready</p>
  <span class="enroll">Enroll now!</span>
</div>
<div class="abs story" style="top:1833px" role="img" aria-label="Chefs in white hats working together in a kitchen"><span>Team ‘LOREM’ creates<br>unbeatable strategy</span></div>
<div class="abs story" style="top:2084px" role="img" aria-label="Chefs in white hats working together in a kitchen"><span>Team ‘LOREM’ creates<br>unbeatable strategy</span></div>
<div class="abs see-more">SEE MORE</div>

<section class="abs compete">
  <h2>START COMPETING</h2>
  <p>Build your own team and start competing<br>against other teams</p>
  <a>Build your team now!</a>
</section>

<section class="abs white-band" style="top:2779px;height:424px"></section>
<div class="abs sponsor" style="left:40px;top:2903px">Lantern Creek<br>Spirits</div>
<div class="abs sponsor" style="left:328px;top:2903px">Red Mesa<br>Rubs</div>
<div class="abs sponsor" style="left:619px;top:2903px">Prairie Cut<br>Meats</div>
<div class="abs sponsor" style="left:929px;top:2903px">Smokehouse<br>Sauce Co.</div>

<footer>
  <div class="abs foot-left"></div>
  <div class="abs foot-right"></div>
  <p class="abs about">Ember Ridge Grilling Society is an organization founded by barbecue cooks for barbecue cooks and our main goal is to bring competition barbecue out of the stone age and into the information age...<br>but above all we want to make barbecue fun again!</p>
  <div class="abs rule"></div>
  <div class="abs social"><span><i></i>Chirper</span><span><i></i>Photogram</span><span><i></i>Friendbook</span><span><i></i>Clipcast</span></div>
  <div class="abs contact">
    <div>Call us</div>
    <div>(555) 014-2873</div>
    <div class="gap"></div>
    <div>Address</div>
    <div>1870 Emberline Rd, Cedar Falls, TX 70000</div>
  </div>
  <div class="abs informed">GET INFORMED</div>
  <div class="abs email">
    <span>Email...</span>
    <div class="go">
      <svg width="44" height="44" viewBox="0 0 44 44"><path d="M13 22h17M24 15l7 7-7 7" fill="none" stroke="#ffffff" stroke-width="2.5" stroke-linecap="round" stroke-linejoin="round"/></svg>
    </div>
  </div>
</footer>

</body>
</html>
```